Tidal Coatings business card for residential and commercial painting

A clean, professional design. Easy to read
Eye catching and elegant
Front could have some color variations
On the back of card I would like all black with signature logo

*Attached is my current business card and the items I want displayed

Contact Information for Business Card

Email, phone number, website, and owner name

Font styles to use
Serif

Requirements
Must have
• My logo with cool design and perhaps some paint splatter

```html
<!DOCTYPE html>
<html lang="en">
<head>
<meta charset="utf-8">
<title>Tidal Coatings — Business Card</title>
<link href="https://fonts.googleapis.com/css2?family=Oswald:wght@500;600&family=Arimo:wght@400;700&display=swap" rel="stylesheet">
<style>
  :root {
    --stage: #1f1f1f;
    --brand-blue: #0e74bf;
    --ink: #333438;
    --paper: #ffffff;
    --muted-block: #d9e4ee;
  }
  * { box-sizing: border-box; margin: 0; padding: 0; }
  html, body { width: 1200px; height: 988px; overflow: hidden; }
  body {
    background: var(--stage);
    position: relative;
    font-family: "Arimo", Arial, sans-serif;
  }
  .card {
    position: absolute;
    width: 620px;
    height: 354px;
    border-radius: 22px;
    overflow: hidden;
  }
  /* Back of card */
  .card--back {
    left: 60px; top: 70px;
    background: var(--brand-blue);
    display: flex; flex-direction: column; align-items: center; justify-content: center;
    gap: 34px;
  }
  .wordmark {
    display: flex; align-items: center; gap: 14px;
    font-family: "Oswald", sans-serif;
    font-weight: 600;
    text-transform: uppercase;
    letter-spacing: 1px;
  }
  .wordmark__dot { width: 22px; height: 22px; border-radius: 50%; }
  .card--back .wordmark { font-size: 60px; color: var(--paper); }
  .card--back .wordmark__dot { background: var(--paper); }
  .price-pill {
    background: var(--paper);
    color: var(--ink);
    font-size: 20px;
    padding: 9px 28px;
    border-radius: 30px;
  }
  /* Front of card */
  .card--front {
    left: 520px; top: 560px;
    background: var(--paper);
  }
  .card--front .wordmark {
    position: absolute; left: 52px; top: 70px;
    font-size: 44px; color: var(--brand-blue);
  }
  .card--front .wordmark__dot { background: var(--brand-blue); width: 18px; height: 18px; }
  .motif {
    position: absolute; right: 0; top: 0;
    width: 190px; height: 354px;
    background: linear-gradient(180deg, var(--brand-blue) 0 28%, var(--ink) 28% 100%);
    border-bottom-left-radius: 18px;
  }
  .edge-tab {
    position: absolute; left: 0; top: 230px;
    width: 18px; height: 52px;
    background: var(--brand-blue);
  }
  .owner { position: absolute; left: 52px; top: 190px; }
  .owner__name {
    font-family: "Arimo", sans-serif; font-weight: 700;
    font-size: 28px; color: var(--brand-blue); line-height: 1;
  }
  .owner__title { font-size: 15px; color: var(--ink); margin-top: 4px; }
  .contact { position: absolute; left: 52px; top: 262px; list-style: none; }
  .contact__item {
    display: flex; align-items: center; gap: 9px;
    font-size: 17px; color: var(--ink); line-height: 26px;
  }
  .contact__item--phone { font-size: 20px; }
  .contact__icon { width: 15px; height: 15px; fill: var(--brand-blue); flex: none; }
</style>
</head>
<body>

<section class="card card--back">
  <div class="wordmark"><span class="wordmark__dot"></span>Tidal Coatings</div>
  <div class="price-pill">Write down a price $$</div>
</section>

<section class="card card--front">
  <div class="wordmark"><span class="wordmark__dot"></span>Tidal Coatings</div>
  <div class="motif" role="img" aria-label="Large decorative brand motif area in blue and charcoal"></div>
  <div class="edge-tab"></div>

  <div class="owner">
    <p class="owner__name">Marco “Mo”</p>
    <p class="owner__title">Owner-Licensed &amp; Insured</p>
  </div>

  <ul class="contact">
    <li class="contact__item contact__item--phone">
      <svg class="contact__icon" viewBox="0 0 16 16" aria-hidden="true"><path d="M3.5 1l2.5 3-1.5 1.8c.9 2 2.4 3.5 4.5 4.5L10.8 9l3.2 2.5-1.3 2.8C7 14 2 9 1.7 3.3z"/></svg>
      555.014.2290
    </li>
    <li class="contact__item">
      <svg class="contact__icon" viewBox="0 0 16 16" aria-hidden="true"><path d="M1 3h14v10H1z M1.8 3.8L8 9l6.2-5.2" stroke="#fff" stroke-width="1.2"/></svg>
      tidalcoatingstn@mailbox.com
    </li>
    <li class="contact__item">
      <svg class="contact__icon" viewBox="0 0 16 16" aria-hidden="true"><circle cx="8" cy="8" r="7"/><path d="M1 8h14M8 1c-3 3.5-3 10.5 0 14M8 1c3 3.5 3 10.5 0 14" stroke="#fff" stroke-width="1" fill="none"/></svg>
      www.tidalcoatingsco.com
    </li>
  </ul>
</section>

</body>
</html>
```